An Agro-Processor Needs a Packaging Design

We need packaging designs for a range of dried fruits and jams with a family look. The line-up has five variants of dried fruits and five variants of jams (the designs to include front and back of the packaging). The entire range will be marketed under the 'Verdyx' brand name - please find the logo attached (the logo has a lock-up with the tagline). The packaging format for the dried fruits are resealable stand-up pouches and the jams are glass bottles - please find attached pictures of the packaging formats for reference.

Please find inspiration boards for the packaging design. Also find attached inspiration board for the design style required for the back of the dried fruit packaging.

For the dried fruit packaging, we need to develop a seal that conveys organic and sugar-free claims (please find attached example of a seal)

Target Market(s)

Organic and natural living enthusiasts who would pay a premium to get the best for them and their families

Industry/Entity Type

Food Production

Font styles to use
Sans Serif
Script

Colors

Designer to choose colors to be used in the design.

Requirements
Must have
• - The brand name 'verdyx' is inspired by the abundance of nature in Africa, it also connotes organic, natural, freshness, delicateness, airiness, sophistication and premium and therefore the design should project these values
• - The design styling to be fun, modern and 'simplistic'
• - Please find below the packaging copy for both dried fruits and jams
• DRIED FRUIT FRONT PACKAGING:
• LOGO: Verdyx - Sunshine in Every Bite
• FIVE VARIANT NAMES: Jolly Pineapple | Dreamy Mango | Breezy Banana | Cheeky Papaya | Dapper Jackfruit
• Dried
• DEVELOP A SEAL: 100% Organic | No Added Sugar (please see example attached)
• Ugandan Origin
• Net Weight: 100g
• DRIED FRUIT BACK COPY:
• Nature's best tasting fruits are also the healthiest which is why we have made it our mission to spread nature's love! Nourished by the tropical rains on the sun-drenched soils of Africa and cultivated by the caring hands of the local farmers, our organic range of dried fruits are nutrient-dense, high in fiber and rich in minerals. Enjoy them in your salads and cereals or simply relish them as a snack! They are diet-friendly if eaten in moderation and are a natural source of energy.
• VISUAL: Stack of Fruit Visual with arrows, each with the following claims (see examples attached in the inspiration boards):
• - 100% Organic
• - No Added Sugar
• - Nutrient-Dense
• - High in Fiber
• - Rich in Minerals
• INCLUDE: Nutritional Facts Table
• Ingredients: Mango - contains 100% fruit with no added sugars, preservatives, additives, colorings or flavorings.
• Reseal the pack to maintain freshness. Store in a cool and dry place.
• INCLUDE SPACE FOR: Batch Code / Expiry Date
• Barcode
• Produced by: Kelvane Food Industries, P. O. Box XXXXX, Kampala - Uganda.
• Find out more about us:
• Telephone: +XXX-XXX-XXXXXX
• Email: Info@KelvaneFoodIndustries.example
• www.Sociapage.example/Verdyx
• JAM FRONT COPY:
• FIVE VARIANT NAMES: Jolly Pineapple with a Hint of Ginger | Dreamy Mango with a Kiss of Vanilla | Breezy Banana with a Twist of Chocolate | Cheeky Papaya with a Pinch of Cardamon | Dapper Jackfruit with a Touch of Cinnamon
• Jam
• Ugandan Origin
• Net Weight: 400g
• JAM BACK COPY:
• Nature's best tasting fruits are also the healthiest which is why we have made it our mission to spread nature's love! Our range of jams come from fruits that have been nourished by the tropical rains on the sun-drenched soils of Africa and have been cultivated by the caring hands of the local farmers. We pride ourselves on making sure that the jams taste as delicious and look as natural as the perfectly ripened fruit! We then make it even better by pairing it with a hint of spice! Enjoy them in your breakfast or use them as a filling in baking.
• Ingredients: Mango, citric acid, sugar, pectin, vanilla
• Barcode
• Find out more about us:

```html
<!DOCTYPE html>
<html lang="en">
<head>
<meta charset="utf-8">
<title>Verdyx Cheeky Papaya Dried Fruit Pouch</title>
<link href="https://fonts.googleapis.com/css2?family=Alfa+Slab+One&family=Arvo:wght@700&family=Rokkitt:wght@800&family=Oswald:wght@500;600&family=Satisfy&display=swap" rel="stylesheet">
<style>
  :root {
    --backdrop: #e2e2e2;
    --pouch: #f8c7a1;
    --pouch-light: #fbd6b8;
    --band: #5a2a22;
    --plaque: #5b3528;
    --plaque-line: #a47b63;
    --cream: #fbefe3;
    --tagline: #e0507a;
    --green: #1f9a3a;
    --orange: #e8471c;
    --outline: #3a1b10;
    --ink: #1d1d1d;
    --seal: #2f8a3c;
    --seal-dark: #1f6b2c;
    --seal-fill: #eef3e2;
    --seal-centre: #9ccf7a;
  }
  * { margin: 0; padding: 0; box-sizing: border-box; }
  html, body { width: 1200px; height: 1200px; overflow: hidden; background: var(--backdrop); }
  .canvas { position: relative; width: 1200px; height: 1200px; }
  .pouch {
    position: absolute; left: 352px; top: 156px; width: 496px; height: 888px;
    background: linear-gradient(90deg, var(--pouch) 0%, var(--pouch-light) 50%, var(--pouch) 100%);
    border-radius: 14px 14px 10px 10px; overflow: hidden;
  }
  .band-top, .band-bottom { position: absolute; left: 0; width: 100%; background: var(--band); }
  .band-top { top: 0; height: 10px; }
  .band-bottom { bottom: 0; height: 18px; }
  .plaque {
    position: absolute; left: 104px; top: 68px; width: 288px; height: 136px;
    background: var(--plaque); border-radius: 34px;
    display: flex; flex-direction: column; align-items: center; justify-content: center;
  }
  .plaque::after {
    content: ""; position: absolute; inset: 9px; border: 2px dotted var(--plaque-line); border-radius: 26px;
  }
  .brand-name { font-family: "Arvo", serif; font-weight: 700; font-size: 50px; color: var(--cream); line-height: 1; }
  .brand-tagline { font-family: "Satisfy", cursive; font-size: 17px; color: var(--tagline); margin-top: 6px; }
  .variant-adjective {
    position: absolute; top: 222px; width: 100%; text-align: center;
    font-family: "Alfa Slab One", serif; font-size: 60px; letter-spacing: 6px; color: var(--green);
    -webkit-text-stroke: 1.5px #0d4a1c; line-height: 1;
  }
  .variant-fruit {
    position: absolute; top: 294px; left: 0; width: 100%; text-align: center;
    font-family: "Rokkitt", serif; font-weight: 800; font-size: 112px; letter-spacing: 18px;
    color: var(--orange); -webkit-text-stroke: 2px var(--outline); line-height: 1;
    transform: scaleX(0.66); transform-origin: center;
  }
  .product-type {
    position: absolute; top: 396px; width: 100%; text-align: center;
    font-family: "Arvo", serif; font-weight: 700; font-size: 36px; color: var(--ink); letter-spacing: 1px;
  }
  .fruit-visual { position: absolute; left: 36px; top: 440px; width: 432px; height: 330px; }
  .seal { position: absolute; left: 52px; top: 736px; width: 88px; height: 88px; }
  .seal-text { font-family: "Oswald", sans-serif; font-weight: 600; font-size: 8px; letter-spacing: 1px; fill: var(--seal-dark); }
  .origin { position: absolute; left: 402px; top: 766px; width: 60px; text-align: center; }
  .origin svg { display: block; margin: 0 auto; }
  .origin-label { font-family: "Oswald", sans-serif; font-weight: 500; font-size: 8px; color: var(--ink); letter-spacing: 0.3px; margin-top: 3px; }
  .net-weight {
    position: absolute; top: 834px; width: 100%; text-align: center;
    font-family: "Oswald", sans-serif; font-weight: 600; font-size: 17px; color: var(--ink); letter-spacing: 0.5px;
  }
</style>
</head>
<body>
<div class="canvas">
  <div class="pouch">
    <div class="band-top"></div>

    <div class="plaque">
      <span class="brand-name">verdyx</span>
      <span class="brand-tagline">Sunshine in Every Bite</span>
    </div>

    <div class="variant-adjective">Cheeky</div>
    <div class="variant-fruit">PAPAYA</div>
    <div class="product-type">= Dried Fruit =</div>

    <svg class="fruit-visual" viewBox="0 0 432 330" role="img" aria-label="Illustration of whole and halved ripe papayas with black seeds">
      <defs>
        <radialGradient id="papayaTone" cx="50%" cy="50%" r="55%">
          <stop offset="0%" stop-color="#f39a2a"/>
          <stop offset="55%" stop-color="#e9632a"/>
          <stop offset="100%" stop-color="#3f9a4a"/>
        </radialGradient>
      </defs>
      <ellipse cx="216" cy="165" rx="212" ry="158" fill="url(#papayaTone)" opacity="0.85"/>
    </svg>

    <svg class="seal" viewBox="0 0 88 88" role="img" aria-label="Seal: 100% Organic, No Added Sugar">
      <defs>
        <path id="sealTop" d="M 14 44 A 30 30 0 0 1 74 44"/>
        <path id="sealBottom" d="M 12 44 A 32 32 0 0 0 76 44"/>
      </defs>
      <circle cx="44" cy="44" r="43" fill="var(--seal)"/>
      <circle cx="44" cy="44" r="40" fill="none" stroke="var(--seal-fill)" stroke-width="1" stroke-dasharray="1.5 2"/>
      <circle cx="44" cy="44" r="37" fill="var(--seal-fill)"/>
      <circle cx="44" cy="44" r="20" fill="var(--seal-fill)" stroke="var(--seal)" stroke-width="1.5"/>
      <circle cx="44" cy="44" r="14" fill="var(--seal-centre)" role="img" aria-label="Leaf sprout"/>
      <text class="seal-text"><textPath href="#sealTop" startOffset="50%" text-anchor="middle">100% ORGANIC</textPath></text>
      <text class="seal-text"><textPath href="#sealBottom" startOffset="50%" text-anchor="middle" dominant-baseline="hanging">NO ADDED SUGAR</textPath></text>
    </svg>

    <div class="origin">
      <svg width="46" height="36" viewBox="0 0 46 36" aria-hidden="true">
        <rect y="0" width="46" height="6" fill="#111"/>
        <rect y="6" width="46" height="6" fill="#f6d000"/>
        <rect y="12" width="46" height="6" fill="#d2161e"/>
        <rect y="18" width="46" height="6" fill="#111"/>
        <rect y="24" width="46" height="6" fill="#f6d000"/>
        <rect y="30" width="46" height="6" fill="#d2161e"/>
        <circle cx="23" cy="18" r="6" fill="#fff"/>
      </svg>
      <div class="origin-label">UGANDAN ORIGIN</div>
    </div>

    <div class="net-weight">Net Weight: 100g</div>

    <div class="band-bottom"></div>
  </div>
</div>
</body>
</html>
```